Spring 2026 Deck Construction Direct Mail Flier

The logo files I will include were named "birchwood valley handymen" by the digital artist. However, my company is called Birchwood Valley Yardcraft (That was not a typo. There is no space between "home" and "service") If you'd like to experiment with color modification of the logo to make it fit better with designs you come up with, please be my guest.

I need a 6"x12" flier design to market my deck construction business. The expected goal is to get phone calls and book appointments for the upcoming Spring 2026 construction season. The call to action being something along the lines of "Call now; Appointments are going fast!"

My target audience is upper middle class (annual household income $100,000 - $200,000) families of 3-5 in the Birchwood Valley of New York state, US. Houses are most commonly either vinyl sided, or sometimes a combination of vinyl siding and brick. The ideal flier design will feature this type of house. Also most houses in my target area have nice lawns with mulched gardens as well.

I prefer designs with more sweeping, gradual curves than sharp square edges and corners, though some squares and corners are ok. I like designs with pallets consisting of blue, red, green, black, gray. I do not like purple, pink, yellow, or orange.

If it's possible and will fit, it would be nice to have images of pressure treated lumber, western cedar decking, and composite decking, so that customers understand I can provide any of the three. Also listing them out would be great.

I prefer designs that are more visual than text-based. On at least one side the dominant element should be a visual of a large composite or cedar deck. An image somewhere - wherever it can fit - of a small (10'x14' or so), basic deck of pressure treated lumber would be ideal as well so that potential clients know I will build those. Also I would like some element, on either side, that creates a sense of urgency by drawing the eye to text along the lines of "2026 appointments are filling fast. Book your free consultation today!"

Selling points:
- Veteran owned and operated
- Hometown feel
- Personal service
- Satisfaction guaranteed

I will use the Northgate General Parcel Corps's "Neighbor Route Drop Delivery" (NRDD) service to deliver these, so on either the front or back there should be a small amount of reserved space in the top right corner for the NGPC's required markings (see https://www.lanternhillprint.com/products/electrician-repair-nrdd-postcard?variant=81736254190 for an example of the amount of space required). It's ok if there is imagery there and it gets covered up by the NGPC markings, it just shouldn't be anything important. You do not have to include the NGPC markings themselves. My print guy will do that when I pass him this design.

A final note on this; I've mentioned Spring 2026 several times. But I do not want the design to be relevant only for Spring. I'd like to use the design throughout the year so please no hard references to Spring that will make the flier seem out of place in the fall.

Thank you very much. I appreciate your time.

```html
<!DOCTYPE html>
<html lang="en">
<head>
<meta charset="utf-8">
<title>Birchwood Valley Yardcraft – Deck Flier</title>
<link rel="stylesheet" href="https://fonts.googleapis.com/css2?family=Poppins:wght@400;500;600;700&family=Saira+Condensed:wght@700;800&display=swap">
<style>
  :root{
    --navy:#14325e;
    --navy-deep:#0e2747;
    --red:#b81f26;
    --red-bright:#d3232a;
    --light:#eef1f6;
    --white:#ffffff;
    --stage:#7f7f7f;
    --green:#2f8a3e;
    --ink:#1b2a44;
  }
  *{box-sizing:border-box;margin:0;padding:0}
  html,body{width:1162px;height:1200px;overflow:hidden}
  body{background:var(--stage);font-family:"Poppins",sans-serif;position:relative}

  .card{position:absolute;left:72px;overflow:hidden;background:var(--navy)}
  .card--front{top:74px;width:1010px;height:504px}
  .card--back{top:638px;width:1012px;height:506px;background:var(--light)}
  .card svg.shapes{position:absolute;inset:0}

  .brand-seal{position:absolute;border-radius:50%;background:var(--white);
    border:4px solid var(--navy);box-shadow:0 0 0 8px rgba(255,255,255,.75);
    display:flex;align-items:center;justify-content:center;text-align:center;
    font-family:"Poppins",sans-serif;font-weight:700;color:var(--navy);
    text-transform:uppercase;line-height:1.15}
  .card--front .brand-seal{left:26px;top:26px;width:168px;height:168px;font-size:16px;padding:18px}
  .card--back .brand-seal{left:542px;top:304px;width:172px;height:172px;font-size:16px;padding:18px}

  /* front */
  .photo-house{position:absolute;left:0;top:0;width:560px;height:400px}
  .welcome{position:absolute;left:511px;top:30px;font-family:"Saira Condensed",sans-serif;
    font-weight:700;font-size:24px;color:var(--navy);line-height:1}
  .headline{position:absolute;left:510px;top:56px;width:325px;font-family:"Saira Condensed",sans-serif;
    font-weight:800;font-size:38px;line-height:.98;letter-spacing:0;white-space:nowrap}
  .headline .line-red{color:var(--red);display:block}
  .headline .line-navy{color:var(--navy);display:block}
  .intro{position:absolute;left:511px;top:136px;width:320px;font-size:10.5px;line-height:1.2;color:var(--ink)}

  .postal-box{position:absolute;z-index:2;left:847px;width:139px;border:2px solid #2a2a2a;background:var(--white);
    font-family:"Poppins",sans-serif;color:#333;text-transform:uppercase}
  .postal-box--indicia{top:23px;height:58px;text-align:center;font-size:8.5px;line-height:1.25;padding-top:4px;font-weight:500}
  .postal-box--indicia .code{font-size:13px;font-weight:600}
  .postal-box--address{top:86px;height:45px;font-size:9px;line-height:1.3;padding:8px 0 0 9px;font-weight:500}

  .material{position:absolute;width:140px;height:140px;border-radius:50%;overflow:hidden;
    border:6px solid var(--red-bright);box-shadow:0 0 0 4px var(--white),0 6px 10px rgba(0,0,0,.25)}
  .material .swatch{position:absolute;inset:0}
  .material .label{position:absolute;left:0;right:0;bottom:0;height:46px;background:var(--white);
    border-radius:50% 50% 0 0/30% 30% 0 0;text-align:center;font-size:10.5px;line-height:1.2;
    color:var(--ink);padding-top:8px;font-weight:500}
  .material--composite{left:510px;top:217px}
  .material--composite .swatch{background:linear-gradient(160deg,#5b6a55 0%,#8a9480 35%,#c9b39a 60%,#d6c2a8 100%)}
  .material--cedar{left:672px;top:183px}
  .material--cedar .swatch{background:linear-gradient(160deg,#3c3a34 0%,#b07a3e 40%,#c8884a 65%,#d9a05e 100%)}
  .material--lumber{left:842px;top:166px;width:144px;height:144px}
  .material--lumber .swatch{background:linear-gradient(170deg,#e6cfa0 0%,#d8b57c 45%,#c99d63 100%)}

  .call-pill{position:absolute;height:40px;background:var(--red);border-radius:0 20px 20px 0;
    color:var(--white);font-weight:600;font-size:23px;line-height:40px;white-space:nowrap}
  .call-pill .phone-badge{position:absolute;left:-26px;top:-7px;width:54px;height:54px;border-radius:50%;
    background:var(--white);border:4px solid var(--red);display:flex;align-items:center;justify-content:center}
  .call-pill .phone-badge svg{width:30px;height:30px}
  .card--front .call-pill{left:644px;top:383px;width:340px;padding-left:44px}
  .card--back .call-pill{left:62px;top:387px;width:328px;padding-left:44px}

  .urgency{position:absolute;color:var(--white);font-weight:700;font-size:30px;letter-spacing:-.5px;white-space:nowrap}
  .card--front .urgency{left:520px;top:430px}
  .card--back .urgency{left:53px;top:436px}

  .contact{position:absolute;color:var(--white);font-weight:400}
  .contact li{list-style:none;display:flex;align-items:center;gap:7px;white-space:nowrap}
  .contact svg{flex:none}
  .card--front .contact{left:44px;top:430px;font-size:18.5px;line-height:22px}
  .card--back .contact{left:729px;top:440px;font-size:12.5px;line-height:16px}

  /* back */
  .photo-worker{position:absolute;left:420px;top:0;width:592px;height:506px;
    background:
      linear-gradient(90deg,var(--light) 0%,rgba(238,241,246,0) 22%),
      linear-gradient(180deg,#5f8fc4 0%,#8fb2d6 14%,rgba(143,178,214,0) 26%),
      linear-gradient(90deg,#b9bcc4 0%,#8f8e95 30%,#a86a48 52%,#c0682f 72%,#b85d2a 100%)}
  .section-title{position:absolute;left:44px;top:30px;font-weight:700;font-size:23px;color:var(--navy);letter-spacing:-.3px}
  .section-title span{color:var(--red)}
  .about{position:absolute;left:44px;top:66px;width:250px;font-size:13px;line-height:16px;color:var(--ink)}
  .perks{position:absolute;left:296px;top:28px;width:200px;list-style:none}
  .perk{position:relative;height:69px;display:flex;align-items:center}
  .perk .perk-badge{width:62px;height:62px;border-radius:50%;background:var(--red);
    border:3px solid var(--white);box-shadow:0 0 0 3px var(--navy);flex:none;
    display:flex;align-items:center;justify-content:center}
  .perk .perk-badge svg{width:30px;height:30px}
  .perk .perk-text{margin-left:9px;font-size:12.4px;line-height:15px;color:var(--navy);font-weight:500}
  .perk + .perk::before{content:"";position:absolute;left:72px;top:-2px;width:96px;border-top:1px dashed var(--red)}
</style>
</head>
<body>

<section class="card card--front" aria-label="Front of flier">
  <svg class="shapes" width="1010" height="504" viewBox="0 0 1010 504">
    <defs>
      <linearGradient id="front-light" x1="0" y1="0" x2="1" y2="0">
        <stop offset="0" stop-color="#dde2ea"/>
        <stop offset="1" stop-color="#ffffff"/>
      </linearGradient>
      <linearGradient id="front-navy" x1="0" y1="0" x2="0" y2="1">
        <stop offset="0" stop-color="#1a3d6e"/>
        <stop offset="1" stop-color="#0e2747"/>
      </linearGradient>
    </defs>
    <rect width="1010" height="504" fill="url(#front-navy)"/>
    <path d="M0 0H1010V276C880 282 720 320 540 372L0 380Z" fill="url(#front-light)"/>
    <path d="M560 330C720 285 860 235 1010 228V258C870 262 720 300 560 352Z" fill="var(--red)"/>
    <path d="M0 370C120 420 300 430 560 380" fill="none" stroke="#ffffff" stroke-width="6"/>
    <path d="M140 38C200 10 270 0 330 0H280C230 6 180 20 140 38Z" fill="var(--red)"/>
  </svg>

  <svg class="photo-house" viewBox="0 0 560 400" role="img" aria-label="Photo: large timber house with wraparound deck, green lawn and landscaped gardens">
    <defs>
      <linearGradient id="house-tone" x1="0" y1="0" x2="0" y2="1">
        <stop offset="0" stop-color="#c9ced6"/>
        <stop offset=".35" stop-color="#7d5a45"/>
        <stop offset=".6" stop-color="#b5552a"/>
        <stop offset=".8" stop-color="#4f8a32"/>
        <stop offset="1" stop-color="#6aa83c"/>
      </linearGradient>
      <linearGradient id="house-fade" x1="0" y1="0" x2="1" y2="0">
        <stop offset=".8" stop-color="#fff" stop-opacity="1"/>
        <stop offset="1" stop-color="#fff" stop-opacity="0"/>
      </linearGradient>
      <mask id="house-mask"><rect width="560" height="400" fill="url(#house-fade)"/></mask>
    </defs>
    <path d="M0 0H560V310C470 350 330 398 180 388C100 383 40 366 0 346Z" fill="url(#house-tone)" mask="url(#house-mask)"/>
  </svg>

  <div class="brand-seal">Birchwood Valley Yardcraft</div>

  <p class="welcome">Welome to</p>
  <h1 class="headline"><span class="line-red">BIRCHWOOD VALLEY</span><span class="line-navy">YARDCRAFT</span></h1>
  <p class="intro">We’re proud to have helped 1,000+ homeowners keep their properties safe, functional, and beautiful.</p>

  <div class="postal-box postal-box--indicia">Presorted Standard<br>NGPC Postage Paid<br>NRDD Retail<br><span class="code">ECRWSS</span></div>
  <div class="postal-box postal-box--address">Local<br>Postal Customer</div>

  <figure class="material material--composite">
    <div class="swatch" role="img" aria-label="Photo: composite deck overlooking a forest"></div>
    <figcaption class="label">Composite<br>decking</figcaption>
  </figure>
  <figure class="material material--cedar">
    <div class="swatch" role="img" aria-label="Photo: western cedar deck by a lake"></div>
    <figcaption class="label">Western<br>cedar decking</figcaption>
  </figure>
  <figure class="material material--lumber">
    <div class="swatch" role="img" aria-label="Photo: stacked pressure treated lumber"></div>
    <figcaption class="label">Pressure<br>treated lumber</figcaption>
  </figure>

  <div class="call-pill">
    <span class="phone-badge"><svg viewBox="0 0 24 24"><path d="M6.6 3.5l2.6 3.4c.4.5.3 1.2-.1 1.6l-1.4 1.3c.9 2 2.5 3.6 4.5 4.5l1.3-1.4c.4-.4 1.1-.5 1.6-.1l3.4 2.6c.5.4.6 1.1.2 1.6l-1.4 2c-.6.8-1.7 1.1-2.6.7C9.9 18 6 14.1 4.3 9.3c-.4-.9-.1-2 .7-2.6l2-1.4" fill="none" stroke="#14325e" stroke-width="1.8" stroke-linejoin="round"/></svg></span>
    Call now (315) 555-0142
  </div>
  <p class="urgency">Appointments are going fast!</p>

  <ul class="contact">
    <li><svg width="20" height="15" viewBox="0 0 20 15"><rect x="1" y="1" width="18" height="13" fill="none" stroke="#fff" stroke-width="1.3"/><path d="M1 1l9 7 9-7M1 14l7-6M19 14l-7-6" fill="none" stroke="#fff" stroke-width="1.3"/></svg>sam@birchwoodvalleyyardcraft.com</li>
    <li><svg width="20" height="20" viewBox="0 0 20 20"><g fill="none" stroke="#fff" stroke-width="1.3"><circle cx="10" cy="10" r="8.5"/><ellipse cx="10" cy="10" rx="4" ry="8.5"/><path d="M1.5 10h17M3 5.5h14M3 14.5h14"/></g></svg>www.birchwoodvalleyyardcraft.com</li>
  </ul>
</section>

<section class="card card--back" aria-label="Back of flier">
  <div class="photo-worker" role="img" aria-label="Photo: builder in a hard hat inspecting a tall stack of lumber"></div>

  <svg class="shapes" width="1012" height="506" viewBox="0 0 1012 506">
    <path d="M760 0C880 40 960 110 1012 190V170C960 95 900 40 820 0Z" fill="var(--red)"/>
    <path d="M0 272C200 255 420 290 640 398L612 410C420 320 210 296 0 316Z" fill="var(--red)"/>
    <path d="M0 330C210 312 420 335 600 412" fill="none" stroke="#fff" stroke-width="5"/>
    <path d="M0 340C220 322 440 350 640 420C660 428 690 430 720 430V506H0Z" fill="var(--navy)"/>
    <ellipse cx="880" cy="470" rx="210" ry="64" fill="var(--green)"/>
  </svg>

  <h2 class="section-title">WHO <span>WE ARE</span></h2>
  <p class="about">Birchwood Valley Yardcraft, we’ve successfully completed 500+ residential and commercial projects across Maple Hollow and the Birchwood Valley. Our skilled team combines over 23 years of experience in residential electrical, custom deck builds, and remodeling solutions. We’re proud to have helped 1,000+ homeowners keep their properties safe, functional, and beautiful.</p>

  <ul class="perks">
    <li class="perk"><span class="perk-badge"><svg viewBox="0 0 24 24" fill="none" stroke="#fff" stroke-width="1.5"><path d="M12 2l2.6 5.3 5.9.9-4.3 4.1 1 5.8L12 15.4 6.8 18.1l1-5.8L3.5 8.2l5.9-.9z"/></svg></span><span class="perk-text">Veteran owned<br>and operated</span></li>
    <li class="perk"><span class="perk-badge"><svg viewBox="0 0 24 24" fill="none" stroke="#fff" stroke-width="1.5" stroke-linejoin="round"><path d="M4 5h16v10H10l-4 4v-4H4z"/></svg></span><span class="perk-text">Personal<br>service</span></li>
    <li class="perk"><span class="perk-badge"><svg viewBox="0 0 24 24" fill="none" stroke="#fff" stroke-width="1.5" stroke-linejoin="round"><path d="M3 11l9-7 9 7M5 10v10h14V10M10 20v-6h4v6"/></svg></span><span class="perk-text">Hometown<br>feel</span></li>
    <li class="perk"><span class="perk-badge"><svg viewBox="0 0 24 24" fill="none" stroke="#fff" stroke-width="1.8" stroke-linecap="round" stroke-linejoin="round"><path d="M5 12.5l4.5 4.5L19 7"/></svg></span><span class="perk-text">Satisfaction<br>guaranteed</span></li>
  </ul>

  <div class="call-pill">
    <span class="phone-badge"><svg viewBox="0 0 24 24"><path d="M6.6 3.5l2.6 3.4c.4.5.3 1.2-.1 1.6l-1.4 1.3c.9 2 2.5 3.6 4.5 4.5l1.3-1.4c.4-.4 1.1-.5 1.6-.1l3.4 2.6c.5.4.6 1.1.2 1.6l-1.4 2c-.6.8-1.7 1.1-2.6.7C9.9 18 6 14.1 4.3 9.3c-.4-.9-.1-2 .7-2.6l2-1.4" fill="none" stroke="#14325e" stroke-width="1.8" stroke-linejoin="round"/></svg></span>
    Call now (315) 555-0142
  </div>
  <p class="urgency">Appointments are going fast!</p>

  <div class="brand-seal">Birchwood Valley Yardcraft</div>

  <ul class="contact">
    <li><svg width="14" height="11" viewBox="0 0 20 15"><rect x="1" y="1" width="18" height="13" fill="none" stroke="#fff" stroke-width="1.5"/><path d="M1 1l9 7 9-7" fill="none" stroke="#fff" stroke-width="1.5"/></svg>sam@birchwoodvalleyyardcraft.com</li>
    <li><svg width="14" height="14" viewBox="0 0 20 20"><g fill="none" stroke="#fff" stroke-width="1.5"><circle cx="10" cy="10" r="8.5"/><ellipse cx="10" cy="10" rx="4" ry="8.5"/><path d="M1.5 10h17"/></g></svg>www.birchwoodvalleyyardcraft.com</li>
  </ul>
</section>

</body>
</html>
```